KORN Tax
Keystone Options and Revenue Navigators
KORN Tax  - Financial Services
Creative Brief
Professional
Tobias Whitlock, CPA CGA
President & CEO
47 Pellam Street Suite 2060 Harborview Court Dartmouth, NS B2C 7K9
rtw@korn.ca
www.korn.ca

```html
<!DOCTYPE html>
<html lang="en">
<head>
<meta charset="utf-8">
<title>KORN Tax – Stationery</title>
<link rel="stylesheet" href="https://fonts.googleapis.com/css2?family=Open+Sans:wght@400;600&display=swap">
<style>
  :root {
    --navy: #0d3a86;
    --blue: #1f5fc4;
    --sky: #5aa9ec;
    --paper: #ffffff;
    --bg: #e9ebee;
    --ink: #4a4f57;
    --muted: #8a9099;
  }
  * { box-sizing: border-box; margin: 0; padding: 0; }
  html, body { width: 1200px; height: 937px; overflow: hidden; }
  body { background: var(--bg); font-family: "Open Sans", Arial, sans-serif; color: var(--ink); position: relative; }

  .sheet { position: absolute; background: var(--paper); overflow: hidden; }
  .wave { position: absolute; left: 0; bottom: 0; width: 100%; display: block; }

  .brand { font-family: "Open Sans", Arial, sans-serif; font-weight: 600; color: var(--navy); line-height: 1.1; white-space: nowrap; }
  .brand-mark { display: inline-block; background: var(--navy); border-radius: 50%; flex: none; }
  .tagline { font-family: "Open Sans", Arial, sans-serif; font-weight: 400; color: var(--ink); letter-spacing: .03em; }

  /* Letterhead */
  .letterhead { left: 182px; top: 63px; width: 393px; height: 544px; }
  .letterhead .logo { position: absolute; left: 30px; top: 34px; display: flex; align-items: center; gap: 8px; }
  .letterhead .brand-mark { width: 16px; height: 16px; }
  .letterhead .brand { font-size: 15px; }
  .letter-body { position: absolute; left: 30px; top: 100px; width: 320px; font-size: 4.6px; line-height: 1.6; color: var(--muted); }
  .letter-body p { margin-bottom: 8px; }
  .signature { width: 40px; height: 14px; margin: 4px 0 6px; display: block; }
  .letter-contact { position: absolute; right: 26px; bottom: 22px; text-align: right; font-size: 4.6px; line-height: 1.7; color: var(--paper); }

  /* Folder */
  .folder { left: 633px; top: 38px; width: 526px; height: 607px; }
  .folder .logo { position: absolute; left: 0; right: 0; top: 200px; display: flex; flex-direction: column; align-items: center; }
  .folder .brand-mark { width: 30px; height: 30px; margin-bottom: 14px; }
  .folder .brand { font-size: 40px; }
  .folder .tagline { font-size: 11px; margin-top: 10px; }
  .folder .site { position: absolute; right: 34px; bottom: 24px; color: var(--paper); font-size: 11px; letter-spacing: .08em; }

  /* Business cards */
  .card-back { left: 46px; top: 678px; width: 192px; height: 102px; }
  .card-back .details { position: absolute; right: 10px; top: 10px; text-align: right; font-size: 4px; line-height: 1.6; color: var(--muted); }
  .card-back .details strong { color: var(--navy); font-size: 5px; }
  .card-front { left: 46px; top: 805px; width: 192px; height: 106px; display: flex; align-items: center; padding-left: 28px; gap: 6px; }
  .card-front .brand-mark { width: 11px; height: 11px; }
  .card-front .brand { font-size: 12px; }

  /* Envelope front */
  .envelope { left: 266px; top: 671px; width: 430px; height: 240px; }
  .envelope .logo { position: absolute; left: 20px; top: 24px; display: flex; align-items: center; gap: 8px; }
  .envelope .brand-mark { width: 16px; height: 16px; }
  .envelope .brand { font-size: 17px; }
  .envelope .site { position: absolute; left: 22px; bottom: 18px; color: var(--paper); font-size: 8px; letter-spacing: .08em; }

  /* Envelope back */
  .envelope-back { left: 734px; top: 671px; width: 430px; height: 240px; }
  .envelope-back .flap { position: absolute; left: 0; top: 0; width: 100%; display: block; }
  .envelope-back .site { position: absolute; right: 34px; top: 30px; color: var(--paper); font-size: 9px; letter-spacing: .08em; }
</style>
</head>
<body>

<section class="sheet letterhead" aria-label="Letterhead">
  <div class="logo">
    <span class="brand-mark"></span>
    <div class="brand">KORN Tax</div>
  </div>
  <div class="letter-body">
    <p>July 2, 2024<br>Client Name<br>12 Sample Lane, Halifax</p>
    <p>Dear Client,</p>
    <p>Thank you for choosing our firm for your annual filing. This letter outlines the next steps we will take together to prepare your return, review your records and plan ahead for the coming year.</p>
    <p>Please gather your receipts, statements and prior notices before our meeting. Our team will review each item carefully and contact you if any further details are needed.</p>
    <p>We value the trust you place in us and look forward to helping your business grow. Do not hesitate to reach out with any questions about your account or our services.</p>
    <p>Sincerely,</p>
    <svg class="signature" viewBox="0 0 40 14"><path d="M2 10 C6 2 9 2 8 9 C12 4 15 4 14 9 C18 5 22 6 24 8 C28 6 32 6 38 5" fill="none" stroke="#333" stroke-width="0.8"/></svg>
    <p>Tobias Whitlock, CPA CGA<br>President &amp; CEO</p>
  </div>
  <svg class="wave" viewBox="0 0 393 150" height="150" preserveAspectRatio="none" aria-hidden="true">
    <path d="M0 95 C110 40 240 125 393 30 L393 150 L0 150 Z" fill="var(--navy)"/>
    <path d="M0 82 C120 28 240 115 393 18" fill="none" stroke="var(--blue)" stroke-width="5"/>
    <path d="M0 72 C130 20 250 100 393 8" fill="none" stroke="var(--sky)" stroke-width="1.5"/>
  </svg>
  <div class="letter-contact">
    47 Pellam Street Suite 2060<br>
    Harborview Court<br>
    Dartmouth, NS B2C 7K9<br>
    Tel 902-555-0147<br>
    Fax 902-555-0148<br>
    rtw@korn.ca<br>
    www.korn.ca
  </div>
</section>

<section class="sheet folder" aria-label="Presentation folder">
  <div class="logo">
    <span class="brand-mark"></span>
    <div class="brand">KORN Tax</div>
    <div class="tagline">Keystone Options and Revenue Navigators</div>
  </div>
  <svg class="wave" viewBox="0 0 526 230" height="230" preserveAspectRatio="none" aria-hidden="true">
    <path d="M0 130 C150 40 330 190 526 60 L526 230 L0 230 Z" fill="var(--navy)"/>
    <path d="M0 112 C160 24 330 170 526 40" fill="none" stroke="var(--blue)" stroke-width="8"/>
    <path d="M0 98 C170 14 340 150 526 22" fill="none" stroke="var(--sky)" stroke-width="2"/>
  </svg>
  <div class="site">www.korn.ca</div>
</section>

<section class="sheet card-back" aria-label="Business card, contact side">
  <div class="details">
    <strong>Tobias Whitlock, CPA CGA</strong><br>
    President &amp; CEO<br>
    Tel 902-555-0147<br>
    rtw@korn.ca<br>
    www.korn.ca
  </div>
  <svg class="wave" viewBox="0 0 192 50" height="50" preserveAspectRatio="none" aria-hidden="true">
    <path d="M0 30 C60 8 120 44 192 12 L192 50 L0 50 Z" fill="var(--navy)"/>
    <path d="M0 24 C60 2 120 38 192 6" fill="none" stroke="var(--sky)" stroke-width="1.5"/>
  </svg>
</section>

<section class="sheet card-front" aria-label="Business card, logo side">
  <span class="brand-mark"></span>
  <div class="brand">KORN Tax</div>
</section>

<section class="sheet envelope" aria-label="Envelope, front">
  <div class="logo">
    <span class="brand-mark"></span>
    <div class="brand">KORN Tax</div>
  </div>
  <svg class="wave" viewBox="0 0 430 130" height="130" preserveAspectRatio="none" aria-hidden="true">
    <path d="M0 80 C140 20 280 100 430 30 L430 130 L0 130 Z" fill="var(--navy)"/>
    <path d="M0 68 C140 10 280 90 430 18" fill="none" stroke="var(--blue)" stroke-width="6"/>
    <path d="M0 58 C150 2 290 78 430 6" fill="none" stroke="var(--sky)" stroke-width="1.5"/>
  </svg>
  <div class="site">www.korn.ca</div>
</section>

<section class="sheet envelope-back" aria-label="Envelope, back">
  <svg class="flap" viewBox="0 0 430 110" height="110" preserveAspectRatio="none" aria-hidden="true">
    <path d="M0 0 L430 0 L430 80 C300 110 150 60 0 95 Z" fill="var(--navy)"/>
    <path d="M0 102 C150 68 300 118 430 88" fill="none" stroke="var(--sky)" stroke-width="1.5"/>
  </svg>
  <div class="site">www.korn.ca</div>
</section>

</body>
</html>
```